Proposal Template Design

We are looking to have our proposal templates redesigned. attached are examples of what we have been using. as well as our current logo

```html
<!DOCTYPE html>
<html lang="en">
<head>
<meta charset="utf-8">
<title>Keystone Foam Works – Letterhead</title>
<link rel="stylesheet" href="https://fonts.googleapis.com/css2?family=Lato:wght@700&family=Open+Sans:wght@400&family=Great+Vibes&display=swap">
<style>
  :root {
    --ink: #231f20;
    --navy: #13233d;
    --sky: #00aeef;
    --sky-soft: #2aa8e0;
    --deep: #0e1620;
    --paper: #ffffff;
  }
  * { margin: 0; padding: 0; box-sizing: border-box; }
  html, body { width: 847px; height: 1200px; overflow: hidden; background: var(--paper); }
  .letterhead {
    position: relative;
    width: 847px;
    height: 1200px;
    background: var(--paper);
    color: var(--ink);
    font-family: "Open Sans", Arial, sans-serif;
  }
  .brand-name {
    position: absolute;
    top: 78px; left: 0; width: 847px;
    text-align: center;
    font-family: "Lato", Arial, sans-serif;
    font-weight: 700;
    font-size: 28px;
    line-height: 34px;
    color: var(--navy);
  }
  .services {
    position: absolute;
    top: 142px; left: 0; width: 847px;
    text-align: center;
    font-family: "Lato", Arial, sans-serif;
    font-weight: 700;
    font-size: 15.5px;
    line-height: 20px;
    color: var(--ink);
  }
  .services .dot { color: var(--sky); }
  .band {
    position: absolute;
    left: 50px;
    width: 731px;
    height: 38px;
  }
  .band--top {
    top: 176px;
    background: linear-gradient(to bottom, var(--sky-soft), var(--deep));
  }
  .band--bottom {
    top: 1107px;
    background: linear-gradient(to bottom, var(--deep), var(--sky-soft));
  }
  .recipient {
    position: absolute;
    top: 282px; left: 112px;
    font-size: 14.2px; line-height: 20.3px;
  }
  .salutation {
    position: absolute;
    top: 364px; left: 563px;
    font-size: 14.2px; line-height: 20px;
  }
  .body-copy {
    position: absolute;
    top: 440px; left: 110px; width: 640px;
    font-size: 14.2px; line-height: 20.3px;
  }
  .body-copy p + p { margin-top: 20.3px; }
  .sign-off { position: absolute; top: 908px; left: 114px; }
  .sign-off__name {
    font-family: "Great Vibes", cursive;
    font-size: 42px; line-height: 44px;
    color: var(--ink);
  }
  .sign-off__role { font-size: 14.2px; line-height: 18px; margin-top: -4px; }
  .contact {
    position: absolute;
    top: 1056px;
    font-size: 15px; line-height: 20.5px;
  }
  .contact--direct { left: 202px; }
  .contact--office { left: 432px; }
  .contact__row { display: flex; align-items: center; }
  .contact__icon { width: 14px; height: 14px; margin-right: 10px; flex: none; }
  .contact__text { white-space: nowrap; }
  .contact__indent { padding-left: 24px; }
</style>
</head>
<body>
<main class="letterhead">
  <div class="brand-name">Keystone Foam Works</div>
  <div class="services">SPRAY FOAM <span class="dot">•</span> FIBERGLASS <span class="dot">•</span> INSULATION <span class="dot">•</span> ROOFING</div>

  <div class="band band--top" role="img" aria-label="Decorative header band in blue and dark navy"></div>

  <div class="recipient">
    Lorem ipsum dolor sit amet,<br>
    consectetuer adipiscing elit, sed<br>
    tincidunt ut laoreet dolore magna<br>
    enim ad minim veniam, quis<br>
    nostrud exerci tation ullamcorp
  </div>
  <div class="salutation">Lorem ipsum dolamet,</div>

  <div class="body-copy">
    <p>Lorem ipsum dolor sit amet, consectetuer adipiscing elit, sed diam nonummy nibh euis-<br>mod tincidunt ut laoreet dolore magna aliquam erat volutpat. Ut wisi enim ad minim<br>veniam, quis nostrud exerci tation ullamcorper suscipit lobortis nisl ut aliquip ex ea com-<br>modo consequat. Duis autem vel eum iriure dolor in hendrerit in vulputate velit esse<br>molestie praesent luptatum zzril delenit augue duis dolore te feugait nulla facilisi.</p>
    <p>Lorem ipsum dolor sit amet, cons ectetuer adipiscing elit, sed diam nonummy nibhquis<br>nostrud exerci tation ullamcorper suscipit lobortis nisl ut aliquip ex ea commodo conse-<br>quat.</p>
    <p>Lorem ipsum dolor sit amet, consectetuer adipiscing elit, sed diam nonummy nibh veniam,<br>quis nostrud exerci tation ullamcorper suscipit lobortis praesent luptatum zzril delenit<br>augue duis dolore te feugait nulla facilisi.</p>
    <p>Lorem ipsum dolor sit amet, cons ectetuer adipiscing elit, sed diam nonummy nibh<br>veniam, quis nostrud exerci tation ullamcorper suscipit lobortis nisl ut aliquip ex ea com-<br>modo consequat.</p>
    <p>Lorem ipsum dolor sit amet, consectetuer adipiscing elit, sed diam nonummy nibh feugiat<br>nulla facilisis at vero eros et accumsan et iusto odio dignissim qui blandit praesent<br>luptatum zzril delenit augue duis dolore te feugait nulla facilisi.</p>
  </div>

  <div class="sign-off">
    <div class="sign-off__name">Lorem ipsum</div>
    <div class="sign-off__role">tincidunt ut laoreet</div>
  </div>

  <div class="contact contact--direct">
    <div class="contact__row">
      <svg class="contact__icon" viewBox="0 0 24 24" aria-hidden="true"><path fill="#00aeef" d="M6.6 10.8a15.1 15.1 0 0 0 6.6 6.6l2.2-2.2c.3-.3.7-.4 1-.2 1.1.4 2.3.6 3.6.6.6 0 1 .4 1 1V20c0 .6-.4 1-1 1A17 17 0 0 1 3 4c0-.6.4-1 1-1h3.5c.6 0 1 .4 1 1 0 1.3.2 2.5.6 3.6.1.3 0 .7-.2 1z"/><path fill="none" stroke="#00aeef" stroke-width="2" d="M14 3a7 7 0 0 1 7 7M14 7a3 3 0 0 1 3 3"/></svg>
      <span class="contact__text">555-014-2297</span>
    </div>
    <div class="contact__row">
      <svg class="contact__icon" viewBox="0 0 24 24" aria-hidden="true"><rect x="2" y="5" width="20" height="14" fill="#00aeef"/><path d="M2 5l10 8 10-8M2 19l8-7M22 19l-8-7" fill="none" stroke="#fff" stroke-width="1.6"/></svg>
      <span class="contact__text">info@keystonefoamworks</span>
    </div>
  </div>

  <div class="contact contact--office">
    <div class="contact__row">
      <svg class="contact__icon" viewBox="0 0 24 24" aria-hidden="true"><path fill="#00aeef" d="M12 1a8 8 0 0 0-8 8c0 6 8 14 8 14s8-8 8-14a8 8 0 0 0-8-8zm0 11a3 3 0 1 1 0-6 3 3 0 0 1 0 6z"/></svg>
      <span class="contact__text">2210 Ridgeline Blvd. Suite 8</span>
    </div>
    <div class="contact__row contact__indent">
      <span class="contact__text">Fairview, TX 75000</span>
    </div>
  </div>

  <div class="band band--bottom" role="img" aria-label="Decorative footer band in dark navy and blue"></div>
</main>
</body>
</html>
```